Young a vibrant Letting agent. New approach to the old market. our colors are various shades of green. We want a clean and clear design with our logo and beautiful shapes. Not too crowded but not too empty. Surprise us!

Size A5, (A4 folded in two)-Cover-Page2-Page3-Back Cover

Once the first and last page is designed, i will send you the content for page 2 and 3

```html
<!DOCTYPE html>
<html lang="en">
<head>
<meta charset="utf-8">
<title>Kestrel Lettings – Brochure Cover</title>
<link href="https://fonts.googleapis.com/css2?family=Open+Sans:wght@700;800&family=PT+Sans&family=Gelasio&display=swap" rel="stylesheet">
<style>
  :root {
    --cream: #f4f1e8;
    --cream-light: #fbfaf5;
    --cream-shade: #e6e0d0;
    --green-dark: #1b5e2c;
    --green-mid: #2e8b3e;
    --green-bright: #6cbf2f;
    --green-pale: #a9d86a;
    --ink: #1e1e1e;
    --fold: #c9c3b3;
    --photo-warm: #c9a57a;
    --photo-light: #ece6dc;
  }
  * { margin: 0; padding: 0; box-sizing: border-box; }
  html, body { width: 1200px; height: 928px; overflow: hidden; background: #fff; }
  .spread {
    position: relative;
    width: 1200px;
    height: 928px;
    overflow: hidden;
    background:
      linear-gradient(155deg, transparent 20%, rgba(255,255,255,.7) 28%, transparent 36%),
      linear-gradient(155deg, transparent 40%, rgba(255,255,255,.55) 46%, transparent 54%),
      linear-gradient(120deg, var(--cream-light) 0%, var(--cream) 45%, var(--cream-shade) 100%);
  }
  .fold-line {
    position: absolute;
    left: 604px; top: 0;
    height: 100%;
    border-left: 1px dashed var(--fold);
  }
  .brand {
    position: absolute;
    left: 642px; top: 34px;
    display: flex; align-items: center; gap: 14px;
    font-family: "Open Sans", sans-serif;
    font-weight: 800;
    font-size: 52px;
    letter-spacing: -1px;
    color: var(--green-dark);
  }
  .brand-mark {
    width: 22px; height: 22px;
    background: var(--green-bright);
  }
  .band { position: absolute; top: 172px; height: 48px; }
  .band-left {
    left: 0; width: 622px;
    background: linear-gradient(90deg, var(--green-dark) 0%, var(--green-mid) 100%);
  }
  .band-title {
    left: 636px; width: 218px;
    background: var(--green-dark);
    color: #fff;
    font-family: "Open Sans", sans-serif;
    font-weight: 700;
    font-size: 30px;
    letter-spacing: 1px;
    display: flex; align-items: center; justify-content: center;
  }
  .band-end {
    left: 866px; width: 114px;
    background: linear-gradient(90deg, var(--green-dark), var(--green-mid));
    border-radius: 0 24px 24px 0;
  }
  .artwork { position: absolute; inset: 0; }
  .contact {
    position: absolute;
    left: 80px; top: 446px;
    width: 400px;
    text-align: center;
    font-family: "Gelasio", serif;
    font-style: normal;
    font-size: 25px;
    line-height: 32px;
    color: var(--ink);
  }
  .contact-city {
    font-family: "PT Sans", sans-serif;
    font-size: 31px;
    line-height: 40px;
    color: var(--green-dark);
  }
</style>
</head>
<body>
<main class="spread">
  <svg class="artwork" width="1200" height="928" viewBox="0 0 1200 928">
    <defs>
      <linearGradient id="photoTone" x1="0" y1="0" x2="1" y2="1">
        <stop offset="0" stop-color="var(--photo-light)"/>
        <stop offset=".55" stop-color="#d9c6ad"/>
        <stop offset="1" stop-color="var(--photo-warm)"/>
      </linearGradient>
      <linearGradient id="swooshTone" x1="0" y1="0" x2="1" y2="0">
        <stop offset="0" stop-color="var(--green-mid)"/>
        <stop offset=".5" stop-color="var(--green-bright)"/>
        <stop offset="1" stop-color="var(--green-pale)"/>
      </linearGradient>
    </defs>
    <path role="img" aria-label="Photo of a smiling young woman holding up house keys among moving boxes in a bright new home"
          d="M0 748 C 110 880, 300 880, 440 770 C 640 600, 860 430, 1200 404 L1200 928 L0 928 Z"
          fill="url(#photoTone)"/>
    <path class="swoosh"
          d="M0 740 C 110 872, 300 872, 440 762 C 640 592, 860 422, 1200 396"
          fill="none" stroke="url(#swooshTone)" stroke-width="12" stroke-linecap="round"/>
    <path d="M0 752 C 110 884, 300 884, 440 774 C 640 604, 860 434, 1200 408"
          fill="none" stroke="var(--green-pale)" stroke-width="3" opacity=".7"/>
  </svg>

  <div class="fold-line"></div>

  <div class="brand"><span class="brand-name">kestrel</span><span class="brand-mark"></span></div>

  <div class="band band-left"></div>
  <div class="band band-title">LETTINGS</div>
  <div class="band band-end"></div>

  <address class="contact">
    <div class="contact-city">Ashbury Vale</div>
    <div>01632 960418</div>
    <div>Harwick: 020 7946 0826</div>
    <div>Email: lettings@kestrel.co.uk</div>
    <div>www.kestrel.co.uk</div>
  </address>
</main>
</body>
</html>
```